Stylish Design With Simple UI For Appointment Site

ONE WEEK TO GO - STILL CONSIDERING NEW DESIGNS!

Note: Logo file now attached. Extra credit to anyone who offers basic HTML templates in the final deliverable, incorporating the individual components of the design (using DIVs and CSS).

There are two key requirements for this site:

1. It makes our site look like one of the most professional of its kind. We want to look the part;
2. It has a very simple, straight-forward user interface. We're nothing without being intuitive.

Our site will be used by other businesses to set up their own online booking systems.

Logo samples attached. The colour scheme is not yet set but two possible options are:

1. Dark (#323B3A) & Blue (#12B5D4) on White background
2. White & Yellow (#FEF102) on Grey (#3A3A3C) background

For inspiration, and an idea of what we like, take a look at quillpost.example - it's very clear and eye-catching, although its pages are longer than we would like ours to be. Oh but we don't need a chimp! Instead of the section with the chimp in, we would like a changing image headline section on the home page, in the style of bellvarine.example.co.uk (with a less high image; we have attached one image which you may want to try out with this, but happy to see other ideas).

Any graphics included must be royalty free and free for commercial use. Fonts should be readily available and specified.

We would like to see the design applied to the following pages:

1. The main public home page (features header, login prompt, menu, changing image banner with headlines, main body, footer menu).
2. A secondary public page (features a similar layout to home page but without image headline banner, includes extra panels/body detail).
3. The Control Panel page (features several list panels and an add appointment button).
4. A list-style administration page (with popup item editor window).
5. A settings administration page (with form).

In that order, a sample walk-through design spec will be attached.

To summarise, we are looking for someone to put forward not only a design but something which also focuses on the user interface. The designer should consider all of the examples and guidance given, but shouldn't let that limit any innovation.

Happy to respond to any questions and give constant feedback.

Thank you.

-*-*-*-*-*-*-*-*-*-*-*-*-*-*-*-*-

Update, 18th Nov 2011:

1. I'm about the upload the logos so you can incorporate these into your designs.

2. A UI question of mine is how to move from a list view (e.g. Resources) to editing one of those items in the list. In the spec document I showed a popup editor for these items but I don't know if that's the best thing to do. Happy to see other ideas on this - whatever the best user experience would be.

3. On the designs in the spec document I've not included any help functionality. It would be good to include pieces of guidance on each page of the administration area to help the user - guess these could either be info panels on the pages themselves or info popups. Again, would be good to see some ideas in the designs.

Also, just to be clear, I am really looking for something that looks like a modern innovative "web app" rather than it looking like a promotional corporate web site.

Target Market(s)

Owners of businesses of all types (e.g. salons, small hotels, surgeries, etc).

Industry/Entity Type

Commercial

Requirements
Must have
• Headline image transition panel on home page.

Layout, graphic and font styles along similar lines to quillpost.example, bellvarine.example.co.uk, etc.
Nice to have
• Blog feed panel on the home page.

Innovative ideas for improvements to the spec.
Should not have
• Anything which can't be practically rendered when the design is converted to HTML.

Should not be overly influenced by the layout and style in the attached spec - that should just be a guide to the content and layout of the site.

```html
<!DOCTYPE html>
<html lang="en">
<head>
<meta charset="utf-8">
<title>Slotwise — Home</title>
<link rel="stylesheet" href="https://fonts.googleapis.com/css2?family=Arvo:wght@400;700&family=Arimo&family=Open+Sans:ital@0;1&family=Oswald:wght@500&display=swap">
<style>
:root{
  --ink:#323b3a;
  --dark:#2a2a2c;
  --panel:#3a3a3c;
  --blue:#12b5d4;
  --teal:#1a8ca3;
  --paper:#f4f4f4;
  --text:#262626;
  --muted:#9a9a9a;
}
*{margin:0;padding:0;box-sizing:border-box}
html,body{width:1200px;height:1118px;overflow:hidden}
body{position:relative;background:var(--paper);font-family:'Arimo',Arial,sans-serif;color:var(--text)}
.top-strip{position:absolute;left:0;top:0;width:1200px;height:7px;background:var(--panel)}
.account-tab{position:absolute;left:882px;top:7px;width:268px;height:43px;background:var(--panel);border-radius:0 0 6px 6px;display:flex;align-items:center;padding-left:20px;gap:10px;box-shadow:0 2px 4px rgba(0,0,0,.25)}
.flag{width:28px;height:18px;background:linear-gradient(#74acdf 33%,#fff 33% 66%,#74acdf 66%)}
.region{font-family:'Open Sans',sans-serif;font-style:italic;color:#eee;font-size:15px;padding-right:14px;border-right:1px dashed #888}
.login-btn{margin-left:2px;width:98px;height:30px;border-radius:4px;border:2px solid #0e5b6a;background:linear-gradient(#5fd3ea,#1394ad);font-family:'Arvo',serif;font-size:15px;color:#0a3640;display:flex;align-items:center;justify-content:center}
.brand{position:absolute;left:80px;top:82px;display:flex;align-items:center;gap:14px;font-family:'Arvo',serif;font-size:38px;color:var(--ink);letter-spacing:3px}
.brand-dot{width:34px;height:34px;border-radius:50%;background:var(--blue)}
.main-nav a{position:absolute;font-family:'Arvo',serif;font-size:18px;color:var(--ink);text-decoration:none;transform:translate(-50%,-50%)}
.main-nav .current{width:102px;height:102px;border-radius:50%;background:radial-gradient(circle at 50% 35%,#3a3a3c,#1c1c1e);color:#eee;display:flex;align-items:center;justify-content:center;box-shadow:0 2px 4px rgba(0,0,0,.3)}
.slider{position:absolute;left:47px;top:190px;width:1104px;height:354px;border-radius:6px;overflow:hidden;background:#000;box-shadow:0 14px 16px -10px rgba(0,0,0,.45)}
.slide-photo{position:absolute;left:0;top:0;width:730px;height:313px;background:radial-gradient(ellipse at 40% 50%,#e6e6e6,#a8a8a8 60%,#5a5a5a)}
.slide-side{position:absolute;left:730px;top:0;width:374px;height:313px;background:linear-gradient(90deg,#2a2524,#000 30%)}
.headline{position:absolute;right:31px;top:52px;width:330px;text-align:right;font-family:'Arvo',serif;font-size:26px;line-height:31px;color:#fff}
.signup{position:absolute;left:873px;top:233px;width:198px;height:55px;border-radius:5px;border:2px solid #0e5b6a;background:linear-gradient(#6cd8ec,#1390aa 60%,#0f7c93);font-family:'Arvo',serif;font-size:24px;color:#0a3640;display:flex;align-items:center;justify-content:center}
.slider-bar{position:absolute;left:0;top:313px;width:1104px;height:41px;background:linear-gradient(#4a4a4c,#3a3a3c);display:flex;align-items:center;justify-content:space-between}
.slider-bar .step{height:41px;display:flex;align-items:center;gap:4px;padding:0 12px;font-family:'Oswald',sans-serif;font-size:22px;color:#fff;background:#38383a;border-right:1px solid #222}
.slider-bar .step.next{border-right:0;border-left:1px solid #222}
.dots{display:flex;gap:6px}
.dots span{width:14px;height:14px;border-radius:50%;background:#1e1e20;box-shadow:inset 0 1px 2px #000}
.dots .on{background:var(--blue)}
.feature{position:absolute;top:607px;width:350px}
.feature-head{display:flex;align-items:center;height:47px;position:relative}
.feature-icon{width:47px;height:47px;border-radius:50%;background:radial-gradient(circle at 50% 35%,#3c4443,#1f2524);color:var(--blue);font-family:'Arvo',serif;font-size:28px;display:flex;align-items:center;justify-content:center}
.feature-head h2{margin-left:15px;font-family:'Arvo',serif;font-weight:700;font-size:22px;color:var(--teal)}
.feature-head::after{content:"";position:absolute;left:42px;right:4px;bottom:1px;height:2px;background:var(--ink)}
.feature p{margin:15px 0 0 34px;width:298px;font-size:14.5px;line-height:24.7px;text-align:justify;color:var(--text)}
.site-footer{position:absolute;left:0;top:864px;width:1200px;height:254px;background:var(--panel);border-top:2px solid #bbb;border-bottom:3px solid var(--blue)}
.footer-nav a{position:absolute;left:80px;font-family:'Arvo',serif;font-size:18px;color:#fff;text-decoration:none}
.footer-nav .current{color:var(--blue)}
.blog-label{position:absolute;left:315px;top:54px;font-family:'Arvo',serif;font-size:18px;color:#fff}
.blog-label span{color:var(--blue)}
.blog-card{position:absolute;left:318px;top:89px;width:564px;height:114px;background:#2c2c2e;border-radius:4px;padding:14px 26px;font-family:'Open Sans',sans-serif;color:#eee;box-shadow:0 1px 3px #000}
.blog-card h3{font-family:'Arvo',serif;font-weight:400;font-size:18px;color:var(--blue);text-decoration:underline}
.blog-meta{margin:10px 0 0 12px;font-style:italic;font-size:15px;color:#ccc}
.blog-meta em{color:var(--blue)}
.blog-card p{font-size:15px;line-height:18px}
.blog-card p em{color:var(--blue)}
.footer-brand{position:absolute;left:943px;top:60px;width:172px;text-align:center}
.footer-brand .name{display:flex;align-items:center;justify-content:center;gap:10px;font-family:'Arvo',serif;font-size:24px;letter-spacing:2px;color:#fff}
.footer-brand .name i{width:22px;height:22px;border-radius:50%;background:var(--blue)}
.footer-brand small{display:block;margin-top:16px;font-family:'Open Sans',sans-serif;font-size:16px;color:#eee}
</style>
</head>
<body>
<div class="top-strip"></div>
<div class="account-tab"><span class="flag"></span><span class="region">Argentina</span><span class="login-btn">LOGIN</span></div>

<div class="brand"><span class="brand-dot"></span>SLOTWISE</div>

<nav class="main-nav">
  <a href="#" style="left:655px;top:119px">HOME</a>
  <a href="#" class="current" style="left:796px;top:117px">FEATURES</a>
  <a href="#" style="left:942px;top:117px">PRICING</a>
  <a href="#" style="left:1076px;top:117px">CONTACT</a>
</nav>

<section class="slider">
  <div class="slide-photo" role="img" aria-label="Close-up photograph of a clock face with its hands near three"></div>
  <div class="slide-side"></div>
  <p class="headline">The generated Lorem Ipsum is therefore always free from repetition, injected humour, words etc.</p>
  <span class="signup">SIGN UP</span>
  <div class="slider-bar">
    <span class="step"><svg width="10" height="16" viewBox="0 0 10 16"><path d="M8 2 2 8l6 6" fill="none" stroke="#fff" stroke-width="2.5"/></svg>PREVIOUS</span>
    <span class="dots"><span class="on"></span><span></span><span></span></span>
    <span class="step next">NEXT<svg width="10" height="16" viewBox="0 0 10 16"><path d="M2 2l6 6-6 6" fill="none" stroke="#fff" stroke-width="2.5"/></svg></span>
  </div>
</section>

<article class="feature" style="left:59px">
  <div class="feature-head"><span class="feature-icon">!</span><h2>Make yourself available</h2></div>
  <p>The point of using Lorem Ipsum is that it has a more-or-less normal distribution of letters, as opposed to using 'Content here, content here', making it look like readable English. Many desktop publishing packages their.</p>
</article>
<article class="feature" style="left:435px">
  <div class="feature-head"><span class="feature-icon">?</span><h2>What’s happening?</h2></div>
  <p>The point of using Lorem Ipsum is that it has a more-or-less normal distribution of letters, as opposed to using 'Content here, content here', making it look like readable English. Many desktop publishing packages their.</p>
</article>
<article class="feature" style="left:811px">
  <div class="feature-head"><span class="feature-icon">@</span><h2>Some text goes here</h2></div>
  <p>The point of using Lorem Ipsum is that it has a more-or-less normal distribution of letters, as opposed to using 'Content here, content here', making it look like readable English. Many desktop publishing packages their.</p>
</article>

<footer class="site-footer">
  <nav class="footer-nav">
    <a href="#" class="current" style="top:54px">HOME</a>
    <a href="#" style="top:96px">FEATURES</a>
    <a href="#" style="top:138px">PRICING</a>
    <a href="#" style="top:180px">CONTACT US</a>
  </nav>
  <div class="blog-label">FROM THE <span>BLOG</span></div>
  <div class="blog-card">
    <h3>Blog Title Text for a demonstration</h3>
    <div class="blog-meta">by <em>dana.ruelle</em> on <em>21/07/2011</em> • <em>3 comments</em></div>
    <p>The point of using Lorem Ipsum is that it has a more-or-less normal distribution of letters, as opposed to using content will... &nbsp;<em>[read more]</em></p>
  </div>
  <div class="footer-brand">
    <div class="name"><i></i>SLOTWISE</div>
    <small>@2011 Copyright</small>
  </div>
</footer>
</body>
</html>
```